domestic violence campaign

To Whom It May Concern:

We are fully aware that domestic violence can enter anyone’s life at any given time. As women we are faced with many demands as mothers, daughters, wives, sisters, providers, and friends. We often lose ourselves and our confidence. Harbor of Hope (HOH) Transitional Center of Western New York has embarked on a whole new way of intervention and prevention. As a domestic violence survivor I have created a facility and ideals which will enforce a revolution of Domestic Violence victims. For many years, growing up in suburbs of Western New York, I have come to terms with this fight. Domestic Violence can be stopped and prevented. As a domestic violence victim myself, being in live-in facility, as well as six different domestic violence shelters throughout the state, I fled from my domestic violence abuse. Without those temporary facilities, all that comes to my mind is death. They helped me rebuild and save my life but something was missing – zero education, training programs, parenting classes, personal strengthening workshops, on site at all. Considering the limited amount of time (30-45 days in an average shelter) and lack of resources, I was in need of the tools needed to move me from being a victim to having a stable life.
Opening more doors in Western New York is essential with the surrounding agencies and shelters overwhelmed from assisting women of crisis. Many issues have risen, as a result, such as: over-crowding, long waiting lists, and zero educational training with an on-site teaching curriculum. A repeated vicious cycle – victims regressing and not progressing with over 4000 cases of domestic violence reported throughout Erie County. The opening Harbor of Hope (HOH) Transitional Center of Western New York will provide a 9-24 month live-in facility, along with educational and training programs on-site that will serve as important tools to domestic violence victims. These educational based facilities and services are well needed for Western New York. Our trained certified staff will provide endless help to domestic violence victim. They will feel safe as they rebuild their lives and take advantage of our educational curriculum that has been designed to increase awareness and provide steppingstones to move the victims into confident stable independent human beings. Our clients will receive complete educational training, state testing, parenting classes, as well as strengthening, coping, and developing skills here at our facility. Harbor of Hope (HOH) Transitional Center is asking for your support.
Sincerely,
Marlena Brooks
President and CEO/website hohtcq.example
Harbor of Hope (HOH) Transitional Center of WNY

Industry/Entity Type

Training

Requirements
Nice to have
• we have already created our T-shirt/we will like for our T-shirt to be the center of the campaign to T-shirt reads
V IOLENCE
O N
W OMEN
S TOPS the campaign is to raise money so we can open doors and save lives

```html
<!DOCTYPE html>
<html lang="en">
<head>
<meta charset="utf-8">
<title>Harbor of Hope – Domestic Violence Campaign Card</title>
<link rel="stylesheet" href="https://fonts.googleapis.com/css2?family=Carlito:wght@400;700&family=Special+Elite&display=swap">
<style>
  :root {
    --backdrop: #d9d9d9;
    --card-dark: #6e5455;
    --card-light: #8c7878;
    --band: #3b2f30;
    --text-light: #ffffff;
    --title-red: #b3161d;
    --figure-dark: #1a1414;
    --figure-light: #bdbdbd;
  }
  * { margin: 0; padding: 0; box-sizing: border-box; }
  html, body {
    width: 1200px;
    height: 1000px;
    overflow: hidden;
    background: var(--backdrop);
  }
  .card {
    position: absolute;
    left: 101px;
    top: 72px;
    width: 998px;
    height: 855px;
    background: linear-gradient(100deg, var(--card-dark) 0%, #7a6263 45%, var(--card-light) 100%);
    font-family: "Carlito", "Calibri", sans-serif;
    color: var(--text-light);
    overflow: hidden;
  }
  .org-name {
    position: absolute;
    left: 26px;
    top: 18px;
    width: 260px;
    text-align: center;
    font-size: 26px;
    line-height: 34px;
  }
  .donate {
    position: absolute;
    left: 804px;
    top: 16px;
    font-size: 25px;
    line-height: 32px;
  }
  .figure-art {
    position: absolute;
    left: 600px;
    top: 330px;
    width: 398px;
    height: 363px;
    background: radial-gradient(ellipse at 70% 55%, var(--figure-dark) 0%, #3a2d2e 45%, rgba(189,189,189,0.35) 75%, rgba(189,189,189,0) 100%);
  }
  .headline {
    position: absolute;
    left: 0;
    width: 1080px;
    top: 174px;
    text-align: center;
    font-size: 56px;
    font-weight: 400;
    color: var(--title-red);
    text-shadow: 2px 2px 3px rgba(0,0,0,0.55);
  }
  .message {
    position: absolute;
    font-size: 29px;
    white-space: nowrap;
  }
  .message--enter { left: 296px; top: 290px; }
  .message--stop  { left: 59px;  top: 375px; }
  .message--ad    { left: 131px; top: 461px; }
  .message--vows  { left: 273px; top: 533px; }
  .slogan-band {
    position: absolute;
    left: 0;
    top: 693px;
    width: 100%;
    height: 105px;
    background: var(--band);
    display: flex;
    align-items: center;
    justify-content: center;
    font-family: "Special Elite", "Courier New", monospace;
    font-size: 46px;
    letter-spacing: 3px;
    color: #f2f2f2;
  }
</style>
</head>
<body>
  <main class="card">
    <p class="org-name">Harbor of Hope<br>Transitional<br>Center of<br>Western New York</p>
    <p class="donate">Donate Today<br>hohtcq.example</p>

    <div class="figure-art" role="img" aria-label="Silhouette illustration of a woman sitting hunched with her knees drawn up, with a pale shadow figure behind her"></div>

    <h1 class="headline">Domestic Violence</h1>
    <p class="message message--enter">Can enter anyone’s life at any given time</p>
    <p class="message message--stop">Domestic Violence can be stopped or prevented</p>
    <p class="message message--ad">Place your Ad, and speak out take the</p>
    <p class="message message--vows">Vows with HOH</p>

    <div class="slogan-band">VIOLENCE ON WOMEN STOPS NOW</div>
  </main>
</body>
</html>
```